Business Card Design

Just looking for a good designs that looks good with our company logo. I'd like it to be simple and to the point. Just including contact information, our logo, and my name somewhere on the card so future clients know who they're contacting, and a couple services offered. The two images I attached are pictures of our logo. I don't care which color they they are, I just attached both images to give a reference of logo colors depending on the color of the card.
Names: Derek Hallory
Phone: 816-442-7061
Email: greenvalebrush@mailzen.test
Services offered:
Mowing
Fertilization
Aeration
Bed & tree maintenance
and more.
Industry/Entity Type
Business
Contact Information for Business Card
Names: Derek Hallory
Phone: 816-442-7061
Look and feel

```html
<!DOCTYPE html>
<html lang="en">
<head>
<meta charset="utf-8">
<title>Greenvale Lawn – Business Card</title>
<link rel="stylesheet" href="https://fonts.googleapis.com/css2?family=Noto+Serif:ital,wght@0,400;0,700;1,400&display=swap">
<style>
  :root {
    --stage: #d9d9d9;
    --card: #ecedeb;
    --coral: #f26a4b;
    --navy: #33344a;
    --ink: #1d1d24;
    --blue: #4d4faa;
    --square: #1c3f8c;
    --badge-blue: #1d8ccf;
    --badge-navy: #2a1f5c;
  }
  * { margin: 0; padding: 0; box-sizing: border-box; }
  html, body { width: 1200px; height: 960px; overflow: hidden; }
  body {
    background: var(--stage);
    font-family: "Noto Serif", Georgia, serif;
    position: relative;
  }
  .card {
    position: absolute;
    left: 150px; top: 223px;
    width: 900px; height: 514px;
    background: var(--card);
    overflow: hidden;
  }
  .contact {
    position: absolute;
    background: var(--coral);
    color: var(--ink);
    display: flex;
    align-items: center;
    justify-content: flex-end;
    gap: 8px;
    padding: 0 14px;
    height: 46px;
    white-space: nowrap;
  }
  .contact::after {
    content: "";
    width: 12px; height: 12px;
    background: var(--square);
    flex: none;
  }
  .contact--name { left: 505px; top: 52px; width: 380px; color: #fff; font-size: 26px; letter-spacing: 0.5px; }
  .contact--phone { left: 590px; top: 116px; width: 260px; font-size: 25px; letter-spacing: 0.5px; }
  .contact--email { left: 555px; top: 176px; width: 330px; font-size: 18px; }
  .phone-icon { width: 18px; height: 18px; flex: none; }
  .badge {
    position: absolute;
    left: 40px; top: 250px;
    display: flex; align-items: center;
  }
  .badge__mark { width: 64px; height: 40px; background: var(--badge-blue); }
  .badge__strip { width: 140px; height: 24px; background: var(--badge-navy); align-self: flex-start; margin-top: 4px; }
  .brand {
    position: absolute;
    left: 260px; top: 240px;
    display: flex; align-items: center; gap: 14px;
    white-space: nowrap;
  }
  .brand__dot { width: 26px; height: 26px; border-radius: 50%; background: var(--coral); flex: none; }
  .brand__name { font-size: 44px; font-weight: 700; color: var(--navy); letter-spacing: 1px; line-height: 1.2; }
  .services {
    position: absolute;
    left: 170px; top: 318px; width: 500px;
    text-align: center;
    font-style: italic;
    font-size: 25px;
    line-height: 1.22;
  }
  .services__line--blue { color: var(--blue); }
  .services__line--coral { color: var(--coral); }
  .landscape {
    position: absolute;
    left: 0; bottom: 0;
    width: 900px; height: 96px;
    background: linear-gradient(to bottom, rgba(51,52,74,0) 0%, rgba(51,52,74,0.55) 40%, var(--navy) 70%);
  }
</style>
</head>
<body>
  <main class="card">
    <div class="contact contact--name">Derek Hallory</div>
    <div class="contact contact--phone">
      <svg class="phone-icon" viewBox="0 0 24 24" aria-hidden="true">
        <path fill="#1c3f8c" d="M6.6 10.8a15.1 15.1 0 0 0 6.6 6.6l2.2-2.2c.3-.3.7-.4 1-.2 1.1.4 2.3.6 3.6.6.6 0 1 .4 1 1V20c0 .6-.4 1-1 1A17 17 0 0 1 3 4c0-.6.4-1 1-1h3.5c.6 0 1 .4 1 1 0 1.3.2 2.5.6 3.6.1.3 0 .7-.2 1l-2.3 2.2z"/>
      </svg>
      <span>816-442-7061</span>
    </div>
    <div class="contact contact--email">greenvalebrush@mailzen.test</div>

    <div class="badge" aria-hidden="true">
      <div class="badge__mark"></div>
      <div class="badge__strip"></div>
    </div>

    <div class="brand">
      <span class="brand__dot"></span>
      <span class="brand__name">Greenvale Lawn</span>
    </div>

    <p class="services">
      <span class="services__line--blue">Mowing .Fertilization .Aeration</span><br>
      <span class="services__line--coral">Bed and tree maintenance</span><br>
      <span class="services__line--blue">and more ...</span>
    </p>

    <div class="landscape" role="img" aria-label="Silhouette of grassy ground with rows of trees along the bottom edge"></div>
  </main>
</body>
</html>
```